Zielgruppe
Ich bin mit TK-Vorsorge als unabhängiger Versicherungsagent Selbstständig. (www.tk-vorsorge.de)
Ich habe mich auf die Absicherung von biometrischen Risiken spezialisiert - die auch in der Broschüre Thematisiert werden sollen. Das Oberthema der Broschüre ist 'biometrische Risiken'. Dies soll dann auf die Themen: Arbeitskraft, Langlebigkeit und Pflege heruntergebrochen werden.
Zielgruppe sind vor allem junge Menschen, die gerade erst eine Ausbildung gestartet oder ihr Studium beendet haben.
Aufgabenstellung
Das Design sollte die drei Hauptbereiche: Arbeitskraft, Langlebigkeit und Pflege, leicht verständlich dem Kunden veranschaulichen. Texte, Informationen und Grafiken (in der Reihenfolge, so wie ich mir das vorstelle) sind als Datei beigefügt.
Das ganze soll im DIN A4 Format gedruckt werden, wobei ich auf einen Hochwertigen Druck inklusive Druckveredelung hohen Wert lege.

```html
<!DOCTYPE html>
<html lang="de">
<head>
<meta charset="utf-8">
<title>Broschüre – Langlebigkeit</title>
<link rel="stylesheet" href="https://fonts.googleapis.com/css2?family=Montserrat:wght@300;400&family=Orbitron:wght@500&display=swap">
<style>
  :root {
    --paper: #f7f7f6;
    --backdrop: #e6e6e6;
    --ink: #3a3a3a;
    --band: #e0a96a;
    --band-ink: #1c1c1c;
    --photo-light: #e9e7e4;
    --photo-mid: #a8a6a3;
    --photo-dark: #4a4a4a;
  }
  * { margin: 0; padding: 0; box-sizing: border-box; }
  html, body {
    width: 1200px; height: 857px; overflow: hidden;
    background: var(--backdrop);
  }
  .spread {
    position: absolute; left: 0; top: 0;
    width: 1200px; height: 857px;
    display: flex;
  }
  .page {
    position: relative;
    width: 600px; height: 857px;
    overflow: hidden;
  }
  .page--text {
    background: var(--paper);
    box-shadow: inset -18px 0 24px -18px rgba(0,0,0,0.18);
  }
  .body-copy {
    position: absolute;
    left: 120px; top: 90px;
    width: 400px;
    font-family: "Montserrat", sans-serif;
    font-weight: 300;
    font-size: 15px;
    line-height: 1.75;
    color: var(--ink);
    text-align: justify;
    letter-spacing: 0.02em;
  }
  .body-copy p + p { margin-top: 22px; }

  .page--photo { background: var(--photo-mid); }
  .photo {
    position: absolute; inset: 0;
    background:
      linear-gradient(160deg, var(--photo-light) 0%, var(--photo-light) 30%, var(--photo-mid) 60%, var(--photo-dark) 100%);
  }
  .chapter-band {
    position: absolute;
    left: 110px; right: 0; bottom: 150px;
    height: 96px;
    background: var(--band);
    opacity: 0.92;
    display: flex; align-items: center;
    padding: 0 28px 0 40px;
  }
  .chapter-title {
    font-family: "Orbitron", sans-serif;
    font-weight: 500;
    font-size: 22px;
    letter-spacing: 0.24em;
    color: var(--band-ink);
    text-transform: uppercase;
    white-space: nowrap;
    display: flex;
    gap: 18px;
  }
  .chapter-arrows { letter-spacing: 0.08em; }
</style>
</head>
<body>
  <main class="spread">
    <section class="page page--text">
      <div class="body-copy">
        <p>Bitte prüfen Sie regelmäßig die Angaben in den Unterlagen, um sie zu überprüfen und zu aktualisieren.</p>
        <p>Wer schwer erkrankt, verliert nicht nur sein Einkommen, sondern auch seine Pläne.</p>
        <p>Wer früh einen Vertrag abschließt, zahlt dauerhaft weniger. Hinzu kommt: Die Gesundheit ist in jungen Jahren meist am günstigsten.</p>
        <p>Sichern Sie Ihre Arbeitskraft rechtzeitig ab.</p>
      </div>
    </section>
    <section class="page page--photo">
      <div class="photo" role="img" aria-label="Schwarzweißfoto einer Stahlfachwerkbrücke mit Straße und Lichtspuren"></div>
      <div class="chapter-band">
        <h2 class="chapter-title"><span>Langlebigkeit</span><span class="chapter-arrows">&gt;&gt;&gt;</span></h2>
      </div>
    </section>
  </main>
</body>
</html>
```